Home Health Agency Marketing Portfolio Booklet

We need a 4 page plus cover (total of 8 pages including front and back cover) design of a Home health Agency Marketing Booklet.
We specialize in taking care of homebound senior patients who needs specialize nursing and medical services in the comfort of their homes. We would like to see a design showing the caring and compassionate nature of our agency. The design should show a nice clean modern layout with nice font selection. Attached is a copy of our logo that needs to be use in the brochure. The colors of the logo should be use in the design of the brochure.
The design will consist of the Front and back cover, inside pages of the cover will be blank but there will be folded pockets that will need some design/color. The inside 4 pages will be full cover, double sided and will have all the information of the company.
The Marketing booklet will be 9"x 12".

```html
<!DOCTYPE html>
<html lang="en">
<head>
<meta charset="utf-8">
<title>Brightway Home Care — Home Health Marketing Booklet</title>
<link rel="stylesheet" href="https://fonts.googleapis.com/css2?family=Montserrat:wght@500;600;700;800&family=Open+Sans:wght@400;600&family=Oswald:wght@500&display=swap">
<style>
:root{
  --blue:#2b9ad6;
  --blue-deep:#1f87c4;
  --orange:#eea020;
  --olive:#b5a552;
  --teal:#4a9aa6;
  --grey:#a9a9a9;
  --ink:#3a3a3a;
  --paper:#ffffff;
  --stage:#eceef0;
  --head:'Montserrat',sans-serif;
  --body:'Open Sans',sans-serif;
}
*{margin:0;padding:0;box-sizing:border-box}
html,body{width:1200px;height:3000px;overflow:hidden}
body{background:var(--stage);position:relative;font-family:var(--body);color:var(--ink)}
.abs{position:absolute}

/* brand wordmark */
.brand{position:absolute;display:flex;align-items:center;gap:8px;font-family:var(--head);font-weight:700;color:var(--blue);white-space:nowrap;line-height:1}
.brand .dot{border-radius:50%;background:var(--orange);flex:none}

/* folder spread */
.folder{position:absolute;left:58px;top:80px;width:1056px;height:969px;background:var(--paper);box-shadow:0 6px 18px rgba(0,0,0,.12)}
.folder .back-info{position:absolute;left:178px;top:170px;width:176px;text-align:center;font-size:8.5px;line-height:1.4;z-index:2}
.folder .back-info p{margin-top:10px}
.folder .back-info .url{font-weight:600;margin-top:16px;font-size:8px}
.cover-photo{position:absolute;left:528px;top:129px;width:528px;height:411px;background:linear-gradient(160deg,#dfe9ec 0%,#9fcad6 45%,#3fa6c8 75%,#e8eef0 100%)}
.cover-sweep{position:absolute;left:372px;top:129px;width:158px;height:411px;z-index:1}
.band{position:absolute;left:0;top:540px;width:1056px;height:121px;background:linear-gradient(90deg,#8fae9c 0%,var(--blue) 22%,var(--blue) 60%,#7fa58a 85%,var(--olive) 100%)}
.band .edge-photo{position:absolute;left:0;top:0;width:130px;height:121px;background:linear-gradient(90deg,#a7b99a,#6fa7a9 70%,rgba(43,154,214,0))}
.band .phone{position:absolute;left:227px;top:22px;font-family:var(--head);font-weight:600;font-size:31px;color:#fff;display:flex;align-items:center;gap:8px}
.band .phone-note{position:absolute;left:227px;top:64px;width:270px;font-size:7px;line-height:1.35;color:#eaf5fb}
.band .title{position:absolute;left:580px;top:8px;width:460px;text-align:center;font-family:var(--head);font-weight:700;font-size:52px;line-height:1;color:#fff;letter-spacing:1px}
.pocket-gap{position:absolute;left:0;top:661px;width:1056px;height:308px}
.pocket-brand{transform:rotate(180deg)}

/* pages */
.page{position:absolute;width:519px;height:694px;background:var(--paper);box-shadow:0 6px 18px rgba(0,0,0,.12);overflow:hidden}
.page p{font-size:9px;line-height:1.4}
.footer{position:absolute;left:39px;right:30px;top:662px;display:flex;align-items:center;gap:10px;font-size:8px;font-weight:600}
.footer .rule{flex:1;height:1px;background:#bbb}
.photo{position:absolute}
.h-big{font-family:var(--head);font-weight:800;font-size:20px;line-height:1.15;color:#2d2d2d}
.h-big span{color:var(--orange)}
.h-sec{position:absolute;font-family:var(--head);font-weight:700;font-size:13.5px;line-height:1.2}
.h-sec.blue{color:var(--blue)}
.h-sec.orange{color:var(--orange)}
.feature-band{position:absolute;left:0;top:333px;width:519px;height:290px;background:linear-gradient(90deg,#3f9fd2 0%,#6ba5b4 55%,var(--olive) 100%);color:#fff}
.feature-band .h-sec{left:39px;top:22px;color:#fff;font-size:13.5px}
.feature-band .lead{position:absolute;left:39px;top:66px;width:450px;color:#eef6fa}
.feature-item{position:absolute;width:200px;display:flex;gap:10px;align-items:flex-start}
.feature-item p{font-size:8.5px;color:#f2f7f9}
.icon-box{flex:none;width:22px;height:22px;border:1.5px solid #fff;border-radius:4px}
.tile{position:absolute;left:36px;width:141px;height:84px;color:#fff;font-family:var(--head);font-weight:500;font-size:11px;display:flex;flex-direction:column;align-items:center;justify-content:center;gap:6px}
.tile .ring{width:24px;height:24px;border:1.5px solid #fff;border-radius:50%}
.orange-box{position:absolute;left:227px;top:396px;width:263px;height:130px;background:var(--orange);padding:12px 14px;display:flex;flex-direction:column;gap:9px}
.orange-box .row{display:flex;gap:10px;align-items:center;color:#fff}
.orange-box .row p{font-size:8px;line-height:1.3}
.orange-box .ring{flex:none;width:16px;height:16px;border:1.5px solid #fff;border-radius:50%}
.tick-row{display:flex;gap:7px;align-items:flex-start}
.tick-row svg{flex:none;margin-top:2px}
.quote-band{position:absolute;left:0;top:528px;width:519px;height:100px;background:linear-gradient(90deg,#7fb3b4,#a9bfae 60%,#c9ccb6)}
.quote-band .bar{position:absolute;left:39px;top:14px;width:4px;height:72px;background:var(--orange)}
.quote-band p{position:absolute;left:55px;top:14px;font-family:var(--head);font-weight:500;font-size:17px;line-height:1.3;color:#fff}
.stats{position:absolute;left:0;top:0;width:519px;height:207px;background:linear-gradient(120deg,#3b8ea4 0%,#5aa7b3 50%,#8cbcc0 100%)}
.stat{position:absolute;left:48px;display:flex;align-items:center;gap:16px;color:#fff}
.stat .num{font-family:'Oswald',sans-serif;font-weight:500;font-size:44px;width:80px}
.stat .vr{width:1px;height:58px;background:#e8f3f5}
.stat p{width:200px;font-size:8px;line-height:1.35;color:#f1f8f9}
</style>
</head>
<body>

<!-- Folder spread: back cover (left), front cover (right), pockets below -->
<section class="folder" aria-label="Folder outside with pockets">
  <div class="brand" style="left:716px;top:52px;font-size:24px"><span class="dot" style="width:20px;height:20px"></span>Brightway Home Care</div>

  <div class="back-info">
    <div class="brand" style="position:relative;justify-content:center;font-size:13px"><span class="dot" style="width:10px;height:10px"></span>Brightway Home Care</div>
    <p>Caring nurses and aides who visit patients at home.</p>
    <p>Skilled nursing and medical help in the comfort of home.</p>
    <p class="url">www.brightwayhomecare.com</p>
  </div>

  <svg class="cover-sweep" viewBox="0 0 158 411" preserveAspectRatio="none" aria-hidden="true">
    <polygon points="95,0 158,0 158,411 0,411" fill="#f3f4f5"/>
  </svg>
  <div class="cover-photo" role="img" aria-label="Photo of four smiling nurses and doctors in scrubs and white coats"></div>

  <div class="band">
    <div class="edge-photo" role="img" aria-label="Faded photo of a caregiver with a clipboard"></div>
    <div class="phone">
      <svg width="24" height="24" viewBox="0 0 24 24" aria-hidden="true"><path d="M6.6 10.8a15 15 0 0 0 6.6 6.6l2.2-2.2c.3-.3.7-.4 1-.2 1.1.4 2.3.6 3.6.6.6 0 1 .4 1 1V20c0 .6-.4 1-1 1A17 17 0 0 1 3 4c0-.6.4-1 1-1h3.5c.6 0 1 .4 1 1 0 1.3.2 2.5.6 3.6.1.3 0 .7-.2 1z" fill="none" stroke="#fff" stroke-width="1.6"/></svg>
      555 010 2040
    </div>
    <p class="phone-note">Our team offers skilled nursing, therapy and personal care for seniors at home. Call us today to plan a visit and learn how we can help your loved one.</p>
    <div class="title">HOME HEALTH MARKETING</div>
  </div>

  <svg class="pocket-gap" viewBox="0 0 1056 308" preserveAspectRatio="none" aria-hidden="true">
    <polygon points="528,45 476,308 580,308" fill="#fafafa"/>
    <polygon points="528,45 524,45 472,308 476,308" fill="#e3e5e7"/>
    <polygon points="528,45 532,45 584,308 580,308" fill="#e3e5e7"/>
  </svg>

  <div class="brand pocket-brand" style="left:150px;top:812px;font-size:22px"><span class="dot" style="width:18px;height:18px"></span>Brightway Home Care</div>
  <div class="brand pocket-brand" style="left:720px;top:812px;font-size:22px"><span class="dot" style="width:18px;height:18px"></span>Brightway Home Care</div>
</section>

<!-- Page 1 -->
<section class="page" style="left:58px;top:1108px" aria-label="Inside page one">
  <div class="photo" style="left:269px;top:53px;width:250px;height:280px;background:linear-gradient(150deg,#eef4f7 0%,#cfe3ee 45%,#7fb6d8 100%)" role="img" aria-label="Photo of a smiling doctor with a clipboard beside a mother and child"></div>
  <h2 class="h-big abs" style="left:39px;top:50px">ABOUT HEALTHCARE<br><span>BUSINESS</span></h2>
  <p class="abs" style="left:39px;top:118px;width:215px">We bring skilled nurses and trusted aides to seniors who are homebound. Every plan is made with the patient and family, so care stays safe, kind and close to home for as long as it is needed.</p>
  <p class="abs" style="left:39px;top:208px;width:110px">Skilled nursing visits that follow each care plan.</p>
  <p class="abs" style="left:160px;top:208px;width:105px">Therapy at home to help regain daily strength.</p>
  <p class="abs" style="left:39px;top:275px;width:110px">Help with bathing, meals and safe daily routines.</p>
  <p class="abs" style="left:160px;top:275px;width:105px">Close contact with doctors and family members.</p>

  <div class="feature-band">
    <h3 class="h-sec">CARING SUPPORT FOR EVERY PATIENT<br>AND EVERY FAMILY WE SERVE</h3>
    <p class="lead">Our team treats each home as a place of comfort. We listen, we explain each step and we stay in touch so families always know how their loved one is doing each week.</p>
    <div class="feature-item" style="left:39px;top:128px"><span class="icon-box"></span><p>Nurses trained for senior and chronic care needs.</p></div>
    <div class="feature-item" style="left:283px;top:128px"><span class="icon-box"></span><p>Visits planned around the patient's daily routine.</p></div>
    <div class="feature-item" style="left:39px;top:181px"><span class="icon-box"></span><p>Wound care, medicine help and health checks.</p></div>
    <div class="feature-item" style="left:283px;top:181px"><span class="icon-box"></span><p>Clear updates shared with family and doctors.</p></div>
    <div class="feature-item" style="left:39px;top:234px"><span class="icon-box"></span><p>Physical, speech and occupational therapy.</p></div>
    <div class="feature-item" style="left:283px;top:234px"><span class="icon-box"></span><p>Friendly aides for meals, bathing and company.</p></div>
  </div>
  <div class="footer"><span>01</span><span class="rule"></span><span>www.brightwayhomecare.com</span></div>
</section>

<!-- Page 2 -->
<section class="page" style="left:621px;top:1108px" aria-label="Inside page two">
  <div class="tile" style="top:57px;background:var(--grey)"><span class="ring"></span>Lorem Ipsum</div>
  <div class="tile" style="top:141px;background:var(--blue)"><span class="ring"></span>Lorem Ipsum</div>
  <div class="tile" style="top:225px;background:var(--orange)"><span class="ring"></span></div>
  <div class="photo" style="left:177px;top:57px;width:313px;height:252px;background:linear-gradient(135deg,#e9eef1 0%,#c9dbe4 50%,#6fa3c9 100%)" role="img" aria-label="Photo of nurses caring for an elderly woman at home"></div>

  <svg class="abs" style="left:36px;top:338px" width="20" height="20" viewBox="0 0 20 20" aria-hidden="true"><circle cx="10" cy="10" r="8" fill="none" stroke="var(--olive)" stroke-width="1.5"/></svg>
  <p class="abs" style="left:66px;top:336px;width:424px;font-size:8.5px">We visit seniors in their own homes and give skilled care with patience and respect. Our nurses work closely with doctors so each patient gets the right support at the right time.</p>

  <p class="abs" style="left:36px;top:400px;width:170px;font-size:8.5px">Nursing visits planned around the patient.</p>
  <p class="abs" style="left:36px;top:437px;width:170px;font-size:8.5px">Therapy that builds strength and balance.</p>
  <p class="abs" style="left:36px;top:472px;width:170px;font-size:8.5px">Medicine reminders and health checks.</p>
  <p class="abs" style="left:36px;top:507px;width:170px;font-size:8.5px">Friendly aides for daily living needs.</p>

  <div class="orange-box">
    <div class="row"><span class="ring"></span><p>Skilled nurses available seven days a week.</p></div>
    <div class="row"><span class="ring"></span><p>Care plans made with patient and family.</p></div>
    <div class="row"><span class="ring"></span><p>Regular reports shared with the doctor.</p></div>
    <div class="row"><span class="ring"></span><p>Safe, calm and caring visits at home.</p></div>
  </div>

  <h3 class="h-sec blue" style="left:36px;top:555px">PROFESSIONAL HEALTH CARE</h3>
  <p class="abs" style="left:36px;top:578px;width:454px;font-size:8.5px">Our licensed staff bring hospital level skill into a warm home setting. We help patients heal, stay independent and feel cared for every single day.</p>
  <div class="footer"><span>01</span><span class="rule"></span><span>www.brightwayhomecare.com</span></div>
</section>

<!-- Page 3 -->
<section class="page" style="left:58px;top:1858px" aria-label="Inside page three">
  <div class="photo" style="left:0;top:0;width:234px;height:298px;border-bottom-right-radius:90px;background:linear-gradient(160deg,#dfe8ee 0%,#b7cfdc 50%,#8fb3c8 100%)" role="img" aria-label="Photo of medical staff walking down a bright hospital hallway"></div>

  <h3 class="h-sec orange" style="left:252px;top:42px">PROFESSIONAL HEALTH CARE</h3>
  <p class="abs" style="left:252px;top:64px;width:240px;font-size:8px">Our nurses and therapists are licensed, trained and kind. They bring skill and patience to every home visit and treat each patient like family.</p>
  <div class="abs" style="left:252px;top:124px;width:240px;display:flex;flex-direction:column;gap:10px">
    <div class="tick-row"><svg width="9" height="9" viewBox="0 0 10 10" aria-hidden="true"><rect x=".5" y=".5" width="9" height="9" fill="none" stroke="var(--blue)"/><path d="M2 5l2 2 4-4" fill="none" stroke="var(--blue)" stroke-width="1.4"/></svg><p style="font-size:8px">Care plans reviewed often with the doctor.</p></div>
    <div class="tick-row"><svg width="9" height="9" viewBox="0 0 10 10" aria-hidden="true"><rect x=".5" y=".5" width="9" height="9" fill="none" stroke="var(--blue)"/><path d="M2 5l2 2 4-4" fill="none" stroke="var(--blue)" stroke-width="1.4"/></svg><p style="font-size:8px">Help at home after a hospital stay.</p></div>
    <div class="tick-row"><svg width="9" height="9" viewBox="0 0 10 10" aria-hidden="true"><rect x=".5" y=".5" width="9" height="9" fill="none" stroke="var(--blue)"/><path d="M2 5l2 2 4-4" fill="none" stroke="var(--blue)" stroke-width="1.4"/></svg><p style="font-size:8px">Support for long term and chronic illness.</p></div>
  </div>
  <p class="abs" style="left:252px;top:232px;width:240px;font-size:8px;text-align:justify">Each patient starts with a home visit from a nurse who checks health, safety and daily needs. Together with the family we write a care plan, set goals and choose the right mix of nursing, therapy and aide support. We keep the plan up to date as needs change over time.</p>
  <p class="abs" style="left:252px;top:330px;width:240px;font-size:8px;text-align:justify">Our therapists help patients walk, move and speak with more ease, so they can stay active and safe in the home they love.</p>
  <p class="abs" style="left:252px;top:392px;width:240px;font-size:8px;text-align:justify">Aides help with bathing, dressing and meals, and they bring friendly company that lifts the spirit each day.</p>
  <p class="abs" style="left:252px;top:454px;width:240px;font-size:8px;text-align:justify">We stay in close touch with doctors and families so everyone knows how the patient is doing.</p>

  <h3 class="h-sec blue" style="left:39px;top:325px">PROFESSIONAL<br>HEALTH CARE</h3>
  <p class="abs" style="left:39px;top:368px;width:195px;font-size:8px;text-align:justify">We care for seniors who cannot easily leave home. Our staff brings skilled help, kind words and steady support to each visit.</p>
  <p class="abs" style="left:39px;top:436px;width:195px;font-size:8px;text-align:justify">Families trust us because we listen, explain each step and keep their loved one safe.</p>

  <div class="quote-band" role="img" aria-label="Faded photo of a caregiver and patient behind a quote">
    <span class="bar"></span>
    <p>Caring for your loved ones<br>with skill, kindness and<br>respect in their own home.</p>
  </div>
  <div class="footer"><span>01</span><span class="rule"></span><span>www.brightwayhomecare.com</span></div>
</section>

<!-- Page 4 -->
<section class="page" style="left:621px;top:1858px" aria-label="Inside page four">
  <div class="stats" role="img" aria-label="Faded teal photo of a medical worker behind key figures">
    <div class="stat" style="top:30px"><span class="num">20%</span><span class="vr"></span><p>More patients recover at home with regular nurse visits and a clear care plan made with the family and the doctor.</p></div>
    <div class="stat" style="top:114px"><span class="num">47%</span><span class="vr"></span><p>Fewer return trips to the hospital when seniors get skilled nursing, therapy and daily support in their own homes.</p></div>
  </div>

  <div class="photo" style="left:48px;top:269px;width:430px;height:196px;border-radius:14px;background:linear-gradient(90deg,#5cb85c 0%,#2b9ad6 35%,#48b0a0 60%,#7cbf4a 85%,#2b9ad6 100%);opacity:.85" role="img" aria-label="Illustration of linked blue and green gears with medical icons"></div>

  <h3 class="h-sec orange" style="left:48px;top:497px">PROFESSIONAL HEALTH CARE</h3>
  <p class="abs" style="left:48px;top:518px;width:440px;font-size:8px">Our agency joins skilled nursing, therapy and aide services into one caring team, so every senior gets steady support without leaving the comfort of home.</p>
  <div class="abs" style="left:48px;top:566px;width:440px;display:flex;gap:20px">
    <div class="tick-row" style="width:135px"><svg width="9" height="9" viewBox="0 0 10 10" aria-hidden="true"><rect x=".5" y=".5" width="9" height="9" fill="none" stroke="var(--blue)"/><path d="M2 5l2 2 4-4" fill="none" stroke="var(--blue)" stroke-width="1.4"/></svg><p style="font-size:8px">Licensed nurses and caring aides on call.</p></div>
    <div class="tick-row" style="width:135px"><svg width="9" height="9" viewBox="0 0 10 10" aria-hidden="true"><rect x=".5" y=".5" width="9" height="9" fill="none" stroke="var(--blue)"/><path d="M2 5l2 2 4-4" fill="none" stroke="var(--blue)" stroke-width="1.4"/></svg><p style="font-size:8px">Care plans built around each patient.</p></div>
    <div class="tick-row" style="width:135px"><svg width="9" height="9" viewBox="0 0 10 10" aria-hidden="true"><rect x=".5" y=".5" width="9" height="9" fill="none" stroke="var(--blue)"/><path d="M2 5l2 2 4-4" fill="none" stroke="var(--blue)" stroke-width="1.4"/></svg><p style="font-size:8px">Updates shared with family and doctors.</p></div>
  </div>
  <div class="footer"><span>01</span><span class="rule"></span><span>www.brightwayhomecare.com</span></div>
</section>

</body>
</html>
```